Real Estate Card Design

I need a new business card! Below you will find my headshot, the company logo and a copy of my previous business card.

The card must contain the following information:

Dana Welch
Sales Representative
FAIR HARBOUR HOMES REALTY INC BROKERGE
204-517 Maple Ave E, Oshawa ON L1G 4K7
Cell: 905-618-4037 Office:905-481-2696
www.danawelch.com dana@movewithwelch.ca

I would like the card to portray security and class all the while being fresh and contemporary. I hold the key....

```html
<!DOCTYPE html>
<html lang="en">
<head>
<meta charset="utf-8">
<title>Dana Welch – Business Card</title>
<link rel="stylesheet" href="https://fonts.googleapis.com/css2?family=PT+Serif:wght@400;700&family=Roboto:wght@400&display=swap">
<style>
  :root{
    --brand-blue:#00a3e4;
    --ink:#2b2b2b;
    --ink-soft:#454545;
    --paper:#ffffff;
    --backdrop:#e9e4df;
    --photo-dark:#1d2433;
    --photo-light:#cdb79c;
  }
  *{margin:0;padding:0;box-sizing:border-box}
  html,body{width:1200px;height:989px;overflow:hidden;background:var(--backdrop)}
  .card{
    position:absolute;left:60px;top:182px;width:1080px;height:624px;
    background:var(--brand-blue);padding:24px;
    box-shadow:0 10px 24px rgba(0,0,0,.18);
  }
  .card-face{position:relative;width:100%;height:100%;background:var(--paper);overflow:hidden}
  .brand{position:absolute;left:50px;top:40px;display:flex;align-items:center;gap:16px}
  .brand-square{width:64px;height:64px;background:var(--brand-blue);flex:none}
  .brand-name{font-family:"PT Serif",serif;font-weight:700;color:var(--ink);font-size:28px;line-height:1.15;letter-spacing:.5px}
  .agent{position:absolute;left:50px;top:240px;font-family:"PT Serif",serif;color:var(--ink)}
  .agent-name{font-size:40px;font-weight:400;line-height:1.1}
  .agent-title{font-size:24px;margin-top:4px}
  .address{position:absolute;left:50px;top:345px;font-family:"Roboto",sans-serif;font-size:25px;line-height:33px;color:var(--ink-soft)}
  .contacts{position:absolute;left:50px;top:432px;font-family:"Roboto",sans-serif;font-size:25px;color:var(--ink-soft);list-style:none}
  .contacts li{display:flex;align-items:center;height:35px}
  .contacts svg{width:24px;height:24px;fill:var(--brand-blue);margin-right:17px;flex:none}
  .contacts .gap{margin-left:12px}
  .contacts .gap svg{margin-right:8px}
  .headshot{
    position:absolute;right:0;bottom:0;width:440px;height:560px;
    background:linear-gradient(180deg,var(--photo-light) 0%,#a8927a 30%,var(--photo-dark) 58%,var(--photo-dark) 100%);
    border-radius:200px 170px 0 0;
  }
</style>
</head>
<body>
  <div class="card">
    <div class="card-face">
      <div class="brand">
        <div class="brand-square"></div>
        <div class="brand-name">FAIR HARBOUR HOMES<br>REALTY INC BROKERGE</div>
      </div>

      <div class="agent">
        <h1 class="agent-name">Dana Welch</h1>
        <p class="agent-title">Sales Representative</p>
      </div>

      <p class="address">204-517 Maple Ave E,<br>Oshawa ON L1G 4K7</p>

      <ul class="contacts">
        <li>
          <svg viewBox="0 0 24 24" aria-hidden="true"><path d="M6.6 10.8a15.2 15.2 0 0 0 6.6 6.6l2.2-2.2c.3-.3.7-.4 1-.2 1.1.4 2.3.6 3.6.6.6 0 1 .4 1 1V20c0 .6-.4 1-1 1C10.6 21 3 13.4 3 4c0-.6.4-1 1-1h3.5c.6 0 1 .4 1 1 0 1.3.2 2.5.6 3.6.1.3 0 .7-.2 1z"/></svg>
          905-481-2696
          <span class="gap" style="display:flex;align-items:center">
            <svg viewBox="0 0 24 24" aria-hidden="true"><path d="M7 1h10a2 2 0 0 1 2 2v18a2 2 0 0 1-2 2H7a2 2 0 0 1-2-2V3a2 2 0 0 1 2-2zm0 3v15h10V4zm5 16.2a.9.9 0 1 0 0 1.8.9.9 0 0 0 0-1.8z"/></svg>
            905-618-4037
          </span>
        </li>
        <li>
          <svg viewBox="0 0 24 24" aria-hidden="true"><path d="M2 5h20v14H2zm2 2v.4l8 5.2 8-5.2V7zm0 2.8V17h16V9.8l-8 5.2z"/></svg>
          dana@movewithwelch.ca
        </li>
        <li>
          <svg viewBox="0 0 24 24" aria-hidden="true"><circle cx="12" cy="12" r="10"/><path d="M8 6c2 1 3 3 1 4s-2 3 0 4 1 4-1 4M16 5c-2 2 0 3 2 3M15 14c2 0 3 2 2 4" stroke="#fff" stroke-width="1.6" fill="none"/></svg>
          www.danawelch.com
        </li>
      </ul>

      <div class="headshot" role="img" aria-label="Headshot of the agent in a pinstripe suit holding up a house key"></div>
    </div>
  </div>
</body>
</html>
```